mental health business card

Double sided business card with logo on front and practitioners details on back.
The front of card should be while and back either blue or grey to match logo.

Space on back for appointment date and time to be written.

Please note that details are not available yet for address etc as currently moving 4500km across Australia. Just use generic or old info from attached letterhead.
Updates

Dear Designers,

Please note business card is also appointment card must have area where  date and time of clients next appointment can be written in.

Target Market(s)

This is card for patients and colleagues

Industry/Entity Type

Mental Health

Requirements
Must have
• Name
Director / Clinical Psychologist
email
web
phone
phone

Nice to have
• embossing on front of card

```html
<!DOCTYPE html>
<html lang="en">
<head>
<meta charset="utf-8">
<title>Clearview Mental Health – Business Card</title>
<link href="https://fonts.googleapis.com/css2?family=Lato:wght@300;400;700;900&display=swap" rel="stylesheet">
<style>
  :root {
    --page-bg: #eceef0;
    --card-white: #ffffff;
    --ink: #1b1b1b;
    --ink-soft: #3a3a3a;
    --brand-navy: #1d4d78;
    --brand-blue: #1f6e9c;
    --brand-sky: #3aa8c9;
    --brand-deep: #163f66;
    --rule-blue: #2a6a96;
    --write-line: #c3ccd4;
    --steel-grey: #8c8f93;
    --icon-grey: #8a8a8a;
    --text-white: #ffffff;
  }
  * { margin: 0; padding: 0; box-sizing: border-box; }
  html, body {
    width: 1200px; height: 841px; overflow: hidden;
    background: var(--page-bg);
    font-family: "Lato", Arial, sans-serif;
  }
  .canvas {
    position: relative; width: 1200px; height: 841px;
    display: flex; align-items: center; justify-content: center; gap: 40px;
  }
  .card {
    position: relative; width: 540px; height: 309px; overflow: hidden;
    box-shadow: 0 6px 18px rgba(0,0,0,.18);
  }

  /* ---------- details side (white) ---------- */
  .card--details { background: var(--card-white); }
  .rule { position: absolute; left: 24px; right: 24px; height: 1px; background: var(--rule-blue); }
  .rule--top { top: 26px; }
  .rule--mid { top: 118px; }
  .rule--bottom { top: 288px; }

  .brand { position: absolute; display: flex; align-items: center; gap: 12px; }
  .brand__square { width: 50px; height: 50px; background: var(--brand-navy); flex: none; }
  .brand__name { font-weight: 300; color: var(--brand-navy); line-height: 1; text-transform: uppercase; }
  .brand__name span { display: block; }
  .brand__line1 { font-size: 38px; letter-spacing: 1px; }
  .brand__line2 { font-size: 17px; letter-spacing: 2px; margin-top: 3px; }
  .card--details .brand { left: 30px; top: 42px; }

  .role { position: absolute; right: 30px; top: 52px; display: flex; align-items: stretch; gap: 8px; text-align: right; }
  .role__title { font-size: 31px; font-weight: 900; color: var(--ink); line-height: 1; letter-spacing: .5px; }
  .role__subtitle { font-size: 10px; font-weight: 700; color: var(--ink); letter-spacing: .3px; margin-top: 3px; }
  .role__bar { width: 6px; background: linear-gradient(var(--brand-navy), var(--brand-sky)); }

  .contact-band {
    position: absolute; left: 0; right: 0; top: 144px; height: 14px;
    background: linear-gradient(180deg, var(--brand-sky) 0%, var(--brand-blue) 45%, var(--brand-deep) 100%);
  }
  .contact-band::after {
    content: ""; position: absolute; left: 0; right: 0; top: 5px; height: 2px; background: rgba(255,255,255,.6);
  }
  .contact { position: absolute; top: 133px; text-align: center; font-size: 11px; color: var(--ink-soft); line-height: 1.45; white-space: nowrap; }
  .contact--address { left: 14px; width: 160px; }
  .contact--phone { left: 190px; width: 160px; }
  .contact--web { right: 16px; width: 180px; }
  .contact__icon {
    width: 36px; height: 36px; border-radius: 50%; background: var(--icon-grey);
    border: 3px solid #fff; margin: 0 auto 10px; display: flex; align-items: center; justify-content: center;
  }
  .contact__icon svg { width: 18px; height: 18px; }

  .appointment { position: absolute; left: 24px; right: 24px; top: 212px; height: 64px; }
  .appointment__line { position: absolute; left: 0; right: 0; height: 1px; background: var(--write-line); }
  .appointment__line--first { top: 24px; }
  .appointment__line--second { top: 56px; }

  /* ---------- brand side (blue) ---------- */
  .card--brand {
    background: linear-gradient(160deg, var(--brand-sky) 0%, var(--brand-blue) 55%, var(--brand-navy) 100%);
  }
  .card--brand .brand { left: 150px; top: 34px; }
  .card--brand .brand__square { background: var(--text-white); }
  .card--brand .brand__name { color: var(--text-white); }
  .brand-side__edge { position: absolute; left: 0; right: 0; top: 136px; height: 6px; background: var(--brand-deep); }
  .brand-side__band {
    position: absolute; left: 0; right: 0; top: 142px; height: 60px; background: var(--steel-grey);
    padding: 10px 0 0 26px; color: var(--text-white);
  }
  .brand-side__band .role__title { font-size: 22px; color: var(--text-white); }
  .brand-side__band .role__subtitle { font-size: 8px; color: var(--text-white); }
  .brand-side__base {
    position: absolute; left: 0; right: 0; top: 202px; bottom: 0;
    background: linear-gradient(180deg, var(--brand-deep) 0%, var(--brand-navy) 100%);
  }
  .brand-side__base::before {
    content: ""; position: absolute; left: 0; right: 0; top: 10px; height: 3px; background: var(--brand-blue);
  }
</style>
</head>
<body>
<main class="canvas">

  <section class="card card--details" aria-label="Card details side">
    <div class="rule rule--top"></div>

    <div class="brand">
      <div class="brand__square"></div>
      <div class="brand__name"><span class="brand__line1">Clearview</span><span class="brand__line2">Mental Health</span></div>
    </div>

    <div class="role">
      <div>
        <div class="role__title">DIRECTOR</div>
        <div class="role__subtitle">CLINICAL PSYCHOLOGIST</div>
      </div>
      <div class="role__bar"></div>
    </div>

    <div class="rule rule--mid"></div>
    <div class="contact-band"></div>

    <div class="contact contact--address">
      <div class="contact__icon">
        <svg viewBox="0 0 24 24" fill="#fff"><path d="M12 3 2 12h3v9h5v-6h4v6h5v-9h3z"/></svg>
      </div>
      Clearview Mental Health<br>New York 0000
    </div>

    <div class="contact contact--phone">
      <div class="contact__icon">
        <svg viewBox="0 0 24 24" fill="#fff"><path d="M3 8c0-2 3-4 9-4s9 2 9 4v2h-5V8H8v2H3zM7 11h10l3 8H4z"/><circle cx="12" cy="15" r="2" fill="#8a8a8a"/></svg>
      </div>
      + 000 - 0000 - 0000<br>+ 000 - 0000 - 0000
    </div>

    <div class="contact contact--web">
      <div class="contact__icon">
        <svg viewBox="0 0 24 24" fill="none" stroke="#fff" stroke-width="1.8"><circle cx="12" cy="12" r="9"/><ellipse cx="12" cy="12" rx="4" ry="9"/><path d="M3 12h18M5 7h14M5 17h14"/></svg>
      </div>
      admin@clearviewmentalhealth.com<br>www.clearviewmentalhealth.com
    </div>

    <div class="appointment" aria-label="Space to write the next appointment date and time">
      <div class="appointment__line appointment__line--first"></div>
      <div class="appointment__line appointment__line--second"></div>
    </div>

    <div class="rule rule--bottom"></div>
  </section>

  <section class="card card--brand" aria-label="Card brand side">
    <div class="brand">
      <div class="brand__square"></div>
      <div class="brand__name"><span class="brand__line1">Clearview</span><span class="brand__line2">Mental Health</span></div>
    </div>
    <div class="brand-side__edge"></div>
    <div class="brand-side__band">
      <div class="role__title">DIRECTOR</div>
      <div class="role__subtitle">CLINICAL PSYCHOLOGIST</div>
    </div>
    <div class="brand-side__base"></div>
  </section>

</main>
</body>
</html>
```